SEO Friendly Web Design Needed for Leading Software Company

Founded in 1986, TRVQ is the market leader for innovative software solutions for the heavy civil construction industry. Our suite of products, including the bestsellers GirderQuote® and SiteLedger®, are used by more than 40,000 workers every day to improve their proficiency at estimating, job management, resource management, safety and equipment maintenance. TRVQ also offers new mobile applications and cloud computing services so companies can work on a wide array of devices including laptops, tablets and smartphones.

In addition to high quality software, TRVQ is best known for providing world-class customer service, and for its friendly, employee-ownership culture. We offer a full range of professional support options to help customers maximize their software investment including implementation planning, training and INSTANT 24/7 phone support.

Goals, objectives and target audience

The goal of our new layout and design will be to increase conversions, enhance user experience and enhance our SERP rankings.

Our objectives are as follows:
1. Clean and well laid out home page. White space is OK.
2. CTAs in strategic locations throughout to drive conversions and MQLs
3. SEO rich content with appropriate layout to meet our SEO requirements
4. 2 Master Design Templates – Home & Internal
5. Custom Design elements for individual modules

Target Audience:
- Heavy / Civil Construction Industry
- C Level executives or persons in leadership roles who utilize our software
- MEN in the construction industry.

Requirements
Should not have
• Feminine design - our industry is largely male construction workers.
Don't use script or goofy fonts
Don't change the logo, or put it in an image where it is not easily viewable.

```html
<!DOCTYPE html>
<html lang="en">
<head>
<meta charset="utf-8">
<title>TRVQ – Innovative Software for the Construction Industry</title>
<link rel="stylesheet" href="https://fonts.googleapis.com/css2?family=Open+Sans:ital,wght@0,400;0,600;0,700;1,400&display=swap">
<style>
:root{
  --orange:#f39a1e;
  --orange-dark:#d97f0c;
  --charcoal:#4a4a4c;
  --charcoal-dark:#3a3a3c;
  --page:#ececec;
  --text:#333;
  --muted:#666;
  --rule:#d6d6d6;
  --white:#fff;
  --green:#1e9b3c;
}
*{box-sizing:border-box;margin:0;padding:0}
html,body{width:1200px;height:2284px;overflow:hidden}
body{position:relative;background:var(--page);font-family:"Open Sans",Arial,sans-serif;color:var(--text);font-size:10px}
.abs{position:absolute}
a{color:inherit;text-decoration:none}

/* top bar */
.topbar{left:0;top:0;width:1200px;height:32px;background:linear-gradient(#48484a,#333335);color:#bbb;font-size:9px;letter-spacing:.3px}
.topbar .tools{left:183px;top:10px}
.topbar .contact{right:180px;top:10px}
.topbar span{margin:0 6px}

/* header */
.header{left:0;top:32px;width:1200px;height:79px;background:var(--white)}
.brand{left:180px;top:22px;display:flex;align-items:center;gap:10px}
.brand-mark{width:26px;height:26px;background:var(--green)}
.brand-name{font-size:26px;font-weight:700;color:var(--green);letter-spacing:1px}
.brand-tag{font-size:12px;color:#333;line-height:1.15;margin-left:6px}
.nav{left:472px;top:0;height:79px;display:flex;font-size:11px;color:#555}
.nav a{display:flex;align-items:center;padding:0 20px;height:79px}
.nav a.active{background:var(--orange);color:#fff;width:85px;justify-content:center;padding:0}

/* hero */
.hero{left:0;top:111px;width:1200px;height:395px;background:linear-gradient(110deg,#8b97a6 0%,#5f6c7c 40%,#3c4654 100%);overflow:hidden}
.hero-panel{left:0;top:0;width:1200px;height:395px}
.hero-machine{left:503px;top:23px;width:632px;height:372px;background:radial-gradient(ellipse at 55% 55%,#f2c12c 0%,#d99d12 45%,rgba(60,60,60,.0) 75%)}
.hero-copy{left:221px;top:95px;width:290px;color:#fff}
.hero-copy .kicker{border-left:4px solid var(--orange);padding-left:14px;font-size:20px;line-height:1.1}
.hero-copy h1{border-left:4px solid var(--orange);padding-left:14px;font-size:52px;font-weight:600;line-height:1;letter-spacing:-.5px}
.hero-copy p{margin-top:20px;font-size:8px;line-height:1.75;text-transform:uppercase;color:#eee}
.hero-btns{left:219px;top:274px;display:flex;gap:12px}
.btn-grey{width:82px;height:25px;background:linear-gradient(#eee,#bdbdbd);border:1px solid #999;border-radius:3px;font-size:9px;color:#444;display:flex;align-items:center;justify-content:center}
.btn-grey:last-child{width:84px}
.dots{left:582px;top:524px;display:flex;gap:4px}
.dots i{width:11px;height:11px;border-radius:50%;background:#ccc;display:block}
.dots i:first-child{background:#999}

/* section headings */
.h2bar{height:33px;background:var(--charcoal);border-left:5px solid var(--orange);color:#fff;font-size:15px;display:flex;align-items:center;padding-left:15px;text-transform:uppercase}
.h2bar small{font-size:9px;margin-left:5px}

/* feature cells */
.cell{display:flex;gap:14px;width:260px}
.thumb{width:85px;height:64px;border:2px solid #fff;box-shadow:0 1px 3px rgba(0,0,0,.35);flex:none}
.cell h3{font-size:10.5px;font-weight:600;color:#222;margin-top:4px;text-transform:uppercase}
.cell p{font-size:9px;color:#555;line-height:1.6;margin-top:4px;width:155px}
.t1{background:linear-gradient(#7fa3c7,#d8dfe7)}
.t2{background:linear-gradient(#9fb6cf,#b28c58)}
.t3{background:linear-gradient(#8ea0b4,#5d5d5d)}
.t4{background:linear-gradient(#b4c7dd,#6f7f95)}
.t5{background:linear-gradient(#d7dde4,#8b8f96)}
.t6{background:linear-gradient(#a9bdd2,#c9a24e)}
.t7{background:linear-gradient(#c9a97c,#6b4e35)}
.t8{background:linear-gradient(#c7d5e4,#e7e2da)}
.vrule{width:1px;background:var(--rule)}
.news-feature{left:765px;top:606px;width:255px;height:72px;background:linear-gradient(90deg,#6a7a8e,#b5c3d4 60%,#dfe5ec);box-shadow:0 1px 3px rgba(0,0,0,.35)}
.news-feature span{position:absolute;left:8px;bottom:6px;background:#333;color:#fff;font-size:8px;padding:3px 8px;border-left:3px solid var(--orange)}

/* feature overview */
.overview{left:180px;top:923px;width:150px;height:58px;background:var(--charcoal);border-left:5px solid var(--orange);color:#fff;padding:12px 0 0 14px;font-size:13px}
.btn-small{display:inline-block;margin-top:4px;background:linear-gradient(#ddd,#aaa);color:#444;font-size:8px;padding:2px 12px;border-radius:2px}
.overview-text{left:344px;top:930px;width:676px;font-size:9.5px;line-height:1.75;color:#444}

/* who uses */
.globe{left:172px;top:1012px;width:200px;height:200px;border-radius:50%;background:radial-gradient(circle at 40% 40%,#7cc2ef 0%,#2a7fc4 55%,#1d5d96 80%);box-shadow:0 4px 10px rgba(0,0,0,.3)}
.who{left:369px;top:1031px;width:225px;height:157px;background:var(--charcoal);color:#fff;padding:14px 0 0 14px;border-left:0}
.who .line{position:absolute;left:5px;top:14px;width:3px;height:32px;background:var(--orange)}
.who .s{font-size:11px}
.who .b{font-size:20px;line-height:1}
.who p{font-size:8.5px;color:#ddd;margin-top:6px;line-height:1.5;width:200px}
.select-row{display:flex;gap:6px;margin-top:8px}
.select{width:132px;height:18px;background:linear-gradient(#eee,#c8c8c8);font-size:7.5px;font-style:italic;color:#555;padding:3px 7px;border-radius:2px}
.view{width:45px;height:18px;background:linear-gradient(#eee,#c8c8c8);font-size:8px;color:#555;display:flex;align-items:center;justify-content:center;border-radius:2px}
.industries{left:609px;top:1031px;width:411px;height:157px;background:var(--charcoal);border-left:4px solid var(--orange);color:#fff;padding:14px 0 0 20px}
.industries h4{font-size:14px;font-weight:600}
.industries .lab{color:var(--orange);font-size:9px;margin-top:6px}
.ind-grid{display:grid;grid-template-columns:105px 95px 95px 95px;font-size:7.5px;color:#ddd;line-height:1.9;margin-top:2px}
.size-row{display:flex;gap:26px;font-size:7.5px;color:#ddd;margin-top:4px}
.hr{left:180px;width:840px;height:1px;background:var(--rule)}

/* proven process */
.process-text{left:180px;top:1296px;width:840px;font-size:9.5px;line-height:1.7;color:#444}
.benefits{left:180px;top:1339px;width:272px}
.benefits li{list-style:none;height:23px;background:#dcdcdc;margin-bottom:6px;font-size:8px;color:#444;display:flex;align-items:center;padding-left:12px}
.benefits li::before{content:"›";margin-right:6px;color:#777}
.testi-title{left:497px;top:1329px;font-size:17px;font-style:italic;color:#333}
.arrows{display:flex;gap:3px}
.arrows i{width:13px;height:13px;background:#c9c9c9;display:flex;align-items:center;justify-content:center;font-style:normal;font-size:9px;color:#fff}
.quote-mark{font-size:34px;color:#aaa;font-family:Georgia,serif;line-height:1}
.testi-photo{left:536px;top:1378px;width:79px;height:63px;border:2px solid #fff;box-shadow:0 1px 3px rgba(0,0,0,.35);background:linear-gradient(#e5c24f,#9a7d5e)}
.testi-text{left:637px;top:1378px;width:340px;font-size:11px;font-style:italic;line-height:1.6;color:#444}
.guarantee{left:344px;top:1479px;width:523px;height:44px;background:linear-gradient(#6b6b6d,#4a4a4c);border-radius:3px;color:#ddd;font-size:19px;font-style:italic;display:flex;align-items:center;justify-content:center;box-shadow:0 14px 12px -10px rgba(0,0,0,.35)}

/* marketing */
.col-title{font-size:11px;font-weight:600;color:#222;text-transform:uppercase}
.badge{width:88px;height:61px;background:#fff;border:1px solid #ddd;display:flex;align-items:center;justify-content:center}
.badge i{display:block;width:38px;height:38px;border-radius:50%;background:#c9c9c9}
.btn-orange{width:107px;height:22px;background:linear-gradient(#f7ab40,var(--orange-dark));color:#fff;font-size:9px;display:flex;align-items:center;justify-content:center;border-radius:2px}
.news-item{font-size:9.5px;line-height:1.6;color:#333;width:270px}
.news-item em{display:block;color:var(--orange);font-size:8.5px;margin-top:6px}
.social-text{left:743px;top:1662px;width:277px;font-size:9.5px;line-height:1.65;color:#444}
.social-links{left:743px;top:1734px;font-size:8px;color:var(--orange);font-style:italic}
.social-links span{margin:0 10px;color:#aaa;font-style:normal}
.circles{display:flex;gap:4px}
.circles i{width:28px;height:28px;border-radius:50%;background:#cfcfcf;display:block}

/* footer */
.footer{left:0;top:2044px;width:1200px;height:210px;background:var(--charcoal)}
.fcol{top:2059px;font-size:7.8px;color:#ccc;line-height:17.8px;text-transform:uppercase}
.fcol h5{font-size:9px;color:#fff;font-weight:700;border-left:3px solid var(--orange);padding-left:6px;line-height:12px;margin-bottom:4px}
.fcol li{list-style:none;padding-left:10px;position:relative}
.fcol li::before{content:"›";position:absolute;left:0}
.fcol .k{color:var(--orange)}
.fsocial{left:978px;top:2063px;display:flex;flex-direction:column;gap:8px}
.fsocial i{display:block;width:26px;height:26px;border-radius:50%;border:1px solid #777}
.bottombar{left:0;top:2254px;width:1200px;height:30px;background:var(--charcoal-dark);color:#999;font-size:7.5px;display:flex;align-items:center;justify-content:center}
</style>
</head>
<body>

<div class="abs topbar">
  <div class="abs tools">TOOLS :<span>LINK</span>|<span>LINK</span>|<span>BLOG</span></div>
  <div class="abs contact">CONTACT US :<span>SALES</span>|<span>SUPPORT</span></div>
</div>

<header class="abs header">
  <div class="abs brand">
    <span class="brand-mark"></span>
    <span class="brand-name">TRVQ</span>
    <span class="brand-tag">Innovative Software<br>for the Construction Industry</span>
  </div>
  <nav class="abs nav">
    <a class="active">SOFTWARE</a><a>SERVICES</a><a>PRICING</a><a>WHO USES TRVQ</a><a>EVENTS</a><a>ABOUT US</a>
  </nav>
</header>

<section class="abs hero">
  <svg class="abs hero-panel" width="1200" height="395" viewBox="0 0 1200 395">
    <polygon points="0,0 610,0 500,395 0,395" fill="#ffffff" opacity=".14"/>
  </svg>
  <div class="abs hero-machine" role="img" aria-label="Yellow wheel loader with a raised bucket on a quarry site"></div>
  <div class="abs hero-copy">
    <div class="kicker">CONSTRUCTION</div>
    <h1>SOFTWARE</h1>
    <p>Lorem ipsum is simply dummy text of the printing and typesetting industry. Lorem ipsum has been the industry's standard dummy text ever since the 1500s, when an unknown printer took a galley of type and scrambled it to make a type specimen book.</p>
  </div>
  <div class="abs hero-btns"><span class="btn-grey">SOFTWARE</span><span class="btn-grey">SALES</span><span class="btn-grey">DEMO</span></div>
</section>
<div class="abs dots"><i></i><i></i><i></i></div>

<h2 class="abs h2bar" style="left:180px;top:553px;width:542px">Heavy Construction Software Suite (H2)</h2>

<div class="abs" style="left:180px;top:606px;display:grid;grid-template-columns:292px 293px 255px;row-gap:40px">
  <div class="cell"><div class="thumb t1" role="img" aria-label="Engineers reviewing plans"></div><div><h3>Estimating &amp; Bidding H3</h3><p>Content Paragraph / Bulletpoints Key-word rich text</p></div></div>
  <div class="cell"><div class="thumb t2" role="img" aria-label="Building under construction"></div><div><h3>Estimating &amp; Bidding H3</h3><p>Content Paragraph / Bulletpoints Key-word rich text</p></div></div>
  <div></div>
  <div class="cell"><div class="thumb t3" role="img" aria-label="Industrial plant at dusk"></div><div><h3>Estimating &amp; Bidding H3</h3><p>Content Paragraph / Bulletpoints Key-word rich text</p></div></div>
  <div class="cell"><div class="thumb t4" role="img" aria-label="Glass office building"></div><div><h3>Estimating &amp; Bidding H3</h3><p>Content Paragraph / Bulletpoints Key-word rich text</p></div></div>
  <div class="cell"><div class="thumb t5" role="img" aria-label="Steel structure"></div><div><h3>Estimating &amp; Bidding H3</h3><p>Content Paragraph / Bulletpoints Key-word rich text</p></div></div>
  <div class="cell"><div class="thumb t6" role="img" aria-label="Dump truck on site"></div><div><h3>Estimating &amp; Bidding H3</h3><p>Content Paragraph / Bulletpoints Key-word rich text</p></div></div>
  <div class="cell"><div class="thumb t7" role="img" aria-label="Scaffolding and framework"></div><div><h3>Estimating &amp; Bidding H3</h3><p>Content Paragraph / Bulletpoints Key-word rich text</p></div></div>
  <div class="cell"><div class="thumb t8" role="img" aria-label="Worker in a hard hat"></div><div><h3>Estimating &amp; Bidding H3</h3><p>Content Paragraph / Bulletpoints Key-word rich text</p></div></div>
</div>
<div class="abs vrule" style="left:450px;top:610px;height:270px"></div>
<div class="abs vrule" style="left:743px;top:690px;height:190px"></div>
<div class="abs news-feature" role="img" aria-label="Two workers in hard hats at a site"><span>WHAT'S NEW ?</span></div>

<div class="abs overview">FEATURE OVERVIEW<br><span class="btn-small">CTA</span></div>
<p class="abs overview-text">There are many variations of passages of Lorem Ipsum available, but the majority have suffered alteration in some form, by injected humour, or randomised words which don't look even slightly believable. If you are going to use a passage of Lorem Ipsum, you need to be sure there isn't anything embarrassing hidden in the middle of text. All the Lorem Ipsum generators on the Internet tend.</p>

<div class="abs who">
  <span class="line"></span>
  <div style="padding-left:60px;margin-left:-60px"></div>
  <div style="margin-left:15px"><div class="s">WHO</div><div class="b">USES TRVQ?</div>
  <p>See who has the competitive advantage in your state or industry</p>
  <div class="select-row"><span class="select">Select a State :</span><span class="view">VIEW</span></div>
  <div class="select-row"><span class="select">Select an Industry :</span><span class="view">VIEW</span></div></div>
</div>
<div class="abs globe" role="img" aria-label="Globe showing the continents"></div>
<div class="abs industries">
  <h4>WHAT INDUSTRIES USE TRVQ?</h4>
  <div class="lab">SEARCH BY INDUSTRY</div>
  <div class="ind-grid">
    <span>ASPHALT</span><span>INDUSTRY</span><span>INDUSTRY</span><span>INDUSTRY</span>
    <span>PAVING</span><span>INDUSTRY</span><span>INDUSTRY</span><span>INDUSTRY</span>
    <span>COMMERCIAL</span><span>INDUSTRY</span><span>INDUSTRY</span><span>INDUSTRY</span>
  </div>
  <div class="lab">SEARCH BY COMPANY SIZE</div>
  <div class="size-row"><span>0-50</span><span>51-100</span><span>101-499</span><span>500-999</span><span>1000+</span></div>
</div>

<div class="abs hr" style="top:1221px"></div>

<h2 class="abs h2bar" style="left:180px;top:1249px;width:277px">The TRVQ Proven Process (H2)</h2>
<p class="abs process-text">Proven Process Overview paragraph. Sit torquent. Orci ipsum sed Nam nulla, justo euismod, cursus. Purus, ultrices est pede vehicula nec Nunc. Nam vitae, auctor quam urna tincidunt sociosqu. Metus ultricies ornare rhoncus! Sagittis. Nunc.</p>
<ul class="abs benefits">
  <li>PROVEN PROCESS MAIN BENEFIT OVERVIEW</li>
  <li>PROVEN PROCESS MAIN BENEFIT OVERVIEW</li>
  <li>PROVEN PROCESS MAIN BENEFIT OVERVIEW</li>
  <li>PROVEN PROCESS MAIN BENEFIT OVERVIEW</li>
</ul>
<div class="abs testi-title">Quoted Testimonials</div>
<div class="abs arrows" style="left:982px;top:1342px"><i>‹</i><i>›</i></div>
<div class="abs quote-mark" style="left:498px;top:1360px">“</div>
<div class="abs testi-photo" role="img" aria-label="Customer portrait in a hard hat"></div>
<p class="abs testi-text">Quisque est Maecenas habitant accumsan vitae, interdum nonummy dis, erat Cras litora tincidunt platea Aenean lacus nascetur facilisis blandit!</p>
<div class="abs quote-mark" style="left:996px;top:1420px">”</div>
<div class="abs guarantee">TRVQ Proven Process &amp; Money Back Guarantee</div>

<div class="abs hr" style="top:1561px"></div>

<h2 class="abs h2bar" style="left:180px;top:1589px;width:446px">Marketing Message (H2) <small>(AWARDS, PR, NEWS, SOCIAL, TESTIMONIALS, JOBS)</small></h2>

<div class="abs col-title" style="left:180px;top:1639px">Awards</div>
<div class="abs arrows" style="left:340px;top:1639px"><i>‹</i><i>›</i></div>
<div class="abs" style="left:180px;top:1665px;display:grid;grid-template-columns:88px 88px;gap:15px">
  <div class="badge"><i></i></div><div class="badge"><i></i></div>
  <div class="badge"><i></i></div><div class="badge"><i></i></div>
</div>
<div class="abs btn-orange" style="left:268px;top:1818px">View more Awards</div>

<div class="abs vrule" style="left:404px;top:1639px;height:200px"></div>

<div class="abs col-title" style="left:426px;top:1639px">News</div>
<div class="abs arrows" style="left:656px;top:1639px"><i>‹</i><i>›</i></div>
<div class="abs news-item" style="left:426px;top:1664px">Construction Estimating Software Developer Conducts 2013 Estimating Outlook Survey<em>Apr 23, 2013</em></div>
<div class="abs news-item" style="left:426px;top:1734px">Construction Estimating Software Developer Conducts 2013 Estimating Outlook Survey<em>Apr 23, 2013</em></div>
<div class="abs btn-orange" style="left:583px;top:1818px">View more News</div>

<div class="abs vrule" style="left:719px;top:1639px;height:200px"></div>

<div class="abs col-title" style="left:743px;top:1639px">Social Feeds</div>
<p class="abs social-text">There are many variations of passages of Lorem Ipsum available, but the majority have suffered alteration in some form, by injected humour, or randomised words which don't look even slightly believable.</p>
<div class="abs social-links">Replay<span>|</span>Comment<span>|</span>Like</div>
<div class="abs circles" style="left:746px;top:1779px"><i></i><i></i><i></i><i></i><i></i></div>
<div class="abs btn-orange" style="left:912px;top:1818px">View more Reviews</div>

<h2 class="abs h2bar" style="left:180px;top:1890px;width:446px">Work Smarter - Content Resource Section (H2)</h2>
<div class="abs" style="left:180px;top:1946px;display:grid;grid-template-columns:292px 293px 255px">
  <div class="cell"><div class="thumb t7" role="img" aria-label="Interior construction work"></div><div><h3>Estimating &amp; Bidding H3</h3><p>Content Paragraph / Bulletpoints Key-word rich text</p></div></div>
  <div class="cell"><div class="thumb t6" role="img" aria-label="Oil rig silhouette at sunset"></div><div><h3>Estimating &amp; Bidding H3</h3><p>Content Paragraph / Bulletpoints Key-word rich text</p></div></div>
  <div class="cell"><div class="thumb t2" role="img" aria-label="Site supervisor with a clipboard"></div><div><h3>Estimating &amp; Bidding H3</h3><p>Content Paragraph / Bulletpoints Key-word rich text</p></div></div>
</div>
<div class="abs vrule" style="left:450px;top:1946px;height:66px"></div>
<div class="abs vrule" style="left:743px;top:1946px;height:66px"></div>

<footer class="abs footer"></footer>
<div class="abs fcol" style="left:180px"><h5>SOFTWARE</h5><ul><li>GirderQuote</li><li>SiteLedger</li><li>Safety Application</li><li>CrewRouter</li><li>GPS</li><li>FleetCircle</li><li>TankLog</li><li>bidarchive.example</li><li>Mobile Apps</li></ul></div>
<div class="abs fcol" style="left:326px"><h5>SERVICES</h5><ul><li>Cloud Services</li><li>Custom Programming</li><li>Universities</li><li>Instant Support</li><li>Training &amp; Events</li><li>Training Options</li></ul></div>
<div class="abs fcol" style="left:490px"><h5>NEWS</h5><ul><li>Newsroom</li><li>Newsletter</li><li>Press Kit</li><li>Newsletter Subscription</li><li>Training &amp; Events</li><li>Careers At</li><li>TRVQ</li><li>Careers in Construction</li></ul></div>
<div class="abs fcol" style="left:670px"><h5>ABOUT US</h5><ul><li>About TRVQ</li><li>TRVQ Culture Blog</li><li>Our Clients</li><li>Contact/More Info</li><li>The TRVQ Story</li><li>Map &amp; Directions</li><li>Stability</li><li>Why Choose</li><li>TRVQ</li></ul></div>
<div class="abs fcol" style="left:807px"><h5>TRVQ</h5>
  <div><span class="k">SALES :</span> 800-555-0142</div>
  <div><span class="k">SUPPORT :</span> 800-555-0177</div>
  <div><span class="k">EMAIL :</span> INFO@TRVQ.EXAMPLE</div>
  <div>4820 W. Meridian Pkwy</div>
  <div>Stafford Hill, TX 77001</div>
</div>
<div class="abs fsocial"><i></i><i></i><i></i><i></i><i></i></div>
<div class="abs bottombar">© COPYRIGHT 2013 TREVAQUE SYSTEMS GROUP, INC. (TRVQ). ALL RIGHTS RESERVED.</div>

</body>
</html>
```